Kestle Plumbing & Heating Limited needs a service and maintenance contract document design

Kestle Plumbing & Heating Limited are a well established family owned and operated company.

We currently offer installation, service and repair services for gas, plumbing, heating and electrical work. We wish to offer service and maintenance plans for plumbing, heating and electrical for our domestic clients in the UK. We would like the brochure to incorporate our company logo and colours, and reflect the reliable, quality, 5 star service we offer our clients.
I have attached a brochure that a friends company uses to give a good idea of the structure of the plans we wish to offer. We want to give our customers a choice in what packages best suit their needs. However, the pricing structure and certain elements/content of what we offer will be slightly different due to our geographical location.

We would like to have the basic structure of the brochure put in place and the
text content editable to our specific needs. Looking for advice on this but we do have Acrobat DC if we need to edit the text ourselves?

We use our logo with "KESTLE" in white over a grey backgound.

Our website is - www.kestle.example
Facebook and twitter handle is - @KestleHeating

Target Market(s)

UK domestic plumbing, heating, natural gas, LPG and electrical market. Both private homeowners and landlords. Please see both the domestic and landlord document files attached for an idea on what we'd like.

Colors

Designer to choose colors to be used in the design.

Requirements
Must have
• Would like the finished design to incorporate the branding and colours we already use. Professional, Contemporary designs that will stand out above our competition.
• The content of the brochures MUST be very similar in structure to the files I’ve attached to the brief.
• We are having many designs submitted that are just copying our website content. This is not what we are asking for.
• I would like the icons etc to be redesigned so they are ours and not copied.
• Please also see the Landlords brochure attached to the brief. We would like this to be a separate document but to reflect the same design as the homeowner design you submit.
• The content of the documents will need to be re worded for our own use but I'm happy to change this once the design element is in place.
• A4 sized pages as per the example I've attached
• Must be able to attach the document to our website for clients to download.
Nice to have
• A4 sized pages as per the examples I've attached
Should not have
• Please DO NOT copy the content from our website to create our service plan brochures. This is not what we are after. As above, we need the brochures to be like the ones we've provided but made to fit our brand.
• Thank you

```html
<!DOCTYPE html>
<html lang="en">
<head>
<meta charset="utf-8">
<title>Kestle Plumbing &amp; Heating – Brochure Pages</title>
<link rel="stylesheet" href="https://fonts.googleapis.com/css2?family=Open+Sans:wght@300;400;600;700&family=Roboto+Condensed:wght@300;700&display=swap">
<style>
  :root{
    --sheet:#c9c9c9;
    --paper:#ffffff;
    --ink:#2c2c2c;
    --muted:#8a8a8a;
    --rule:#dddddd;
    --blue:#1a66c2;
    --blue-deep:#0b3aa8;
    --blue-bright:#1f7ae0;
    --orange:#f47a20;
    --red:#e8321f;
    --yellow:#f6c21b;
    --tile:#ececec;
  }
  *{box-sizing:border-box;margin:0;padding:0}
  html,body{width:930px;height:1200px;overflow:hidden}
  body{background:var(--sheet);font-family:"Open Sans",Arial,sans-serif;color:var(--ink);position:relative}

  .sheet-label{position:absolute;width:379px;text-align:center;font:600 16px/1 "Open Sans",Arial,sans-serif;color:#222;letter-spacing:.3px}

  .page{position:absolute;width:379px;height:537px;background:var(--paper);overflow:hidden;box-shadow:0 2px 6px rgba(0,0,0,.25)}
  .page--cover{left:84px;top:51px}
  .page--services{left:476px;top:51px}
  .page--welcome{left:84px;top:604px}
  .page--reviews{left:476px;top:604px}

  .page-footer{position:absolute;left:0;bottom:0;width:379px;height:39px}
  .page-footer svg{position:absolute;inset:0}
  .page-footer .url{position:absolute;left:0;right:0;top:6px;text-align:center;color:#fff;font:400 9.5px/1 "Open Sans",Arial,sans-serif;letter-spacing:1.1px}

  .page-header{position:absolute;left:18px;right:18px;top:12px;height:41px;border-bottom:1px solid var(--rule)}
  .wordmark{position:absolute;left:0;top:8px}
  .wordmark-name{display:block;font:700 21px/1 "Roboto Condensed",Arial,sans-serif;color:var(--ink);letter-spacing:3.6px}
  .wordmark-tag{display:block;font:600 4.8px/1 "Open Sans",Arial,sans-serif;color:var(--blue);letter-spacing:3.1px;margin-top:2px}
  .brand-dot{position:absolute;right:0;top:2px;width:33px;height:33px;border-radius:50%;background:var(--blue)}

  .cover-head{position:absolute;left:0;top:0;width:379px;height:97px;background:linear-gradient(180deg,#3c3c3c,#262626)}
  .cover-head .brand-dot{top:20px;left:42px;right:auto;width:58px;height:58px}
  .cover-head .name{position:absolute;left:124px;top:22px;font:700 46px/1 "Roboto Condensed",Arial,sans-serif;color:#fff;letter-spacing:7px}
  .cover-head .tag{position:absolute;left:126px;top:70px;font:600 8.5px/1 "Open Sans",Arial,sans-serif;color:var(--blue-bright);letter-spacing:6.2px}
  .photo{position:absolute}
  .photo--tap{left:0;top:101px;width:93px;height:177px;background:linear-gradient(160deg,#b9a08a,#e8e2da 60%,#c8bfb4)}
  .photo--basin{left:97px;top:101px;width:282px;height:175px;background:linear-gradient(135deg,#cfc8bf,#f1efec 55%,#b6ada2)}
  .photo--kitchen{left:0;top:283px;width:272px;height:213px;background:linear-gradient(160deg,#a3968a,#e4e0dc 50%,#8a6a4e)}
  .photo--boiler{left:277px;top:283px;width:102px;height:213px;background:linear-gradient(180deg,#9a5a44,#e9ecf0 40%,#c9ccd2)}
  .cover-badge{position:absolute;left:96px;top:191px;width:178px;height:178px;border-radius:50%;border:4px solid #fff;background:radial-gradient(circle at 40% 35%,var(--blue-bright),var(--blue-deep));color:#fff;text-align:center;padding-top:46px}
  .cover-badge .lead{font:300 11px/1 "Open Sans",Arial,sans-serif;letter-spacing:.8px}
  .cover-badge .line-light{font:300 26px/1 "Roboto Condensed",Arial,sans-serif;margin-top:6px}
  .cover-badge .line-bold{font:700 26px/1 "Roboto Condensed",Arial,sans-serif}
  .cover-badge .line-big{font:700 31px/1 "Roboto Condensed",Arial,sans-serif;margin-top:1px}
  .cover-badge .rule{width:72px;height:1px;background:rgba(255,255,255,.8);margin:5px auto 0}

  .hero-banner{position:absolute;left:17px;top:62px;width:344px;height:239px;background:linear-gradient(180deg,#3f8fe8 0%,#1d63d3 45%,#0b35a6 100%)}
  .hero-title{position:absolute;left:32px;top:189px;color:#fff;font:700 30px/32px "Roboto Condensed",Arial,sans-serif;text-transform:uppercase}
  .service-grid{position:absolute;left:17px;top:312px;width:344px;display:grid;grid-template-columns:repeat(4,81px);grid-auto-rows:79px;gap:6px 6px}
  .service-tile{background:var(--tile);display:flex;flex-direction:column;align-items:center;padding-top:13px}
  .service-icon{width:36px;height:36px}
  .service-name{margin-top:16px;font:700 5.4px/1 "Open Sans",Arial,sans-serif;color:#333;text-transform:uppercase}

  .welcome-title{position:absolute;left:18px;top:76px;color:var(--blue);font:700 32px/33px "Roboto Condensed",Arial,sans-serif;text-transform:uppercase}
  .about-box{position:absolute;left:18px;top:183px;width:343px;height:120px;background:var(--blue);color:#fff;padding:15px 16px}
  .about-box p{font:400 5.3px/7px "Open Sans",Arial,sans-serif;margin-bottom:6px}
  .seal{position:absolute;left:19px;top:325px;width:152px;height:152px;border-radius:50%;border:2px solid var(--red);display:flex;flex-direction:column;align-items:center;justify-content:center}
  .seal .name{font:700 20px/1 "Roboto Condensed",Arial,sans-serif;color:var(--ink);letter-spacing:3px}
  .seal .tag{font:600 4.4px/1 "Open Sans",Arial,sans-serif;color:var(--blue);letter-spacing:2.6px;margin-top:2px}
  .feature{position:absolute;left:181px;width:182px}
  .feature svg{position:absolute;left:0;top:0}
  .feature h3{margin-left:20px;font:700 7.2px/1 "Open Sans",Arial,sans-serif;color:#222}
  .feature p{margin:5px 0 0 20px;font:400 5.6px/7.2px "Open Sans",Arial,sans-serif;color:#444}

  .reviews-title{position:absolute;left:19px;top:75px;color:var(--blue);font:700 33px/1 "Roboto Condensed",Arial,sans-serif}
  .review-grid{position:absolute;left:19px;top:117px;width:339px;display:grid;grid-template-columns:repeat(3,112px);grid-auto-rows:141px;gap:16px 4px}
  .review{position:relative;text-align:center}
  .review .stars{color:var(--yellow);font-size:7px;letter-spacing:1px;line-height:1;margin-top:6px}
  .review .title{font:400 5.6px/1 "Open Sans",Arial,sans-serif;color:#333;margin-top:3px;white-space:nowrap;overflow:hidden}
  .review .date{font:400 4.3px/1 "Open Sans",Arial,sans-serif;color:var(--blue);margin-top:5px}
  .review .verified{font:400 3.6px/1 "Open Sans",Arial,sans-serif;color:#666;margin-top:4px}
  .ratings{position:absolute;left:2px;right:2px;top:50px;border-top:1px solid var(--rule);padding-top:4px}
  .ratings div{display:flex;justify-content:space-between;font:400 4.2px/7.8px "Open Sans",Arial,sans-serif;color:#444}
  .ratings span:last-child{color:var(--yellow);font-size:5px;letter-spacing:.4px}
  .review .body{position:absolute;left:3px;right:3px;top:88px;font:400 4.1px/5.4px "Open Sans",Arial,sans-serif;color:var(--muted)}
  .share-bar{position:absolute;left:0;right:0;bottom:0;height:12px;background:var(--orange);color:#fff;font:400 4.4px/12px "Open Sans",Arial,sans-serif}
  .partner-row{position:absolute;left:22px;top:438px;width:336px;height:44px;display:flex;justify-content:space-between;align-items:center}
  .partner{background:#dfe3e8}
  .partner--a{width:86px;height:28px;border-radius:4px}
  .partner--b{width:118px;height:26px;border-radius:4px}
  .partner--c{width:38px;height:44px;border-radius:4px;background:#c7ccd2}
  .partner--d{width:42px;height:42px;background:var(--yellow)}
</style>
</head>
<body>

<svg width="0" height="0" style="position:absolute" aria-hidden="true">
  <defs>
    <linearGradient id="footerFlame" x1="0" y1="0" x2="0" y2="1">
      <stop offset="0" stop-color="#f26a1f"/>
      <stop offset="1" stop-color="#f59a1c"/>
    </linearGradient>
    <linearGradient id="iconFlame" x1="0" y1="0" x2="0" y2="1">
      <stop offset="0" stop-color="#f47a20"/>
      <stop offset="1" stop-color="#e8321f"/>
    </linearGradient>
    <symbol id="footer-band" viewBox="0 0 379 39">
      <rect x="0" y="0" width="379" height="39" fill="url(#footerFlame)"/>
      <rect x="0" y="0" width="379" height="17" fill="#222"/>
      <path d="M98 16 C112 16 112 27 126 27 L253 27 C267 27 267 16 281 16 Z" fill="#222"/>
    </symbol>
  </defs>
</svg>

<div class="sheet-label" style="left:84px;top:21px">COVER PAGE</div>
<div class="sheet-label" style="left:476px;top:21px">INNER PAGE 1</div>
<div class="sheet-label" style="left:84px;top:1160px">INNER PAGE 2</div>
<div class="sheet-label" style="left:476px;top:1160px">INNER PAGE 3</div>

<section class="page page--cover">
  <header class="cover-head">
    <span class="brand-dot"></span>
    <span class="name">KESTLE</span>
    <span class="tag">PLUMBING &amp; HEATING</span>
  </header>
  <div class="photo photo--tap" role="img" aria-label="Photo of a chrome tap with running water"></div>
  <div class="photo photo--basin" role="img" aria-label="Photo of a modern bathroom basin and bath"></div>
  <div class="photo photo--kitchen" role="img" aria-label="Photo of a fitted kitchen with a window and sink"></div>
  <div class="photo photo--boiler" role="img" aria-label="Photo of a wall mounted boiler with a test meter"></div>
  <div class="cover-badge">
    <div class="lead">Your Local</div>
    <div class="line-light">PLUMBING</div>
    <div class="line-bold">&amp; HEATING</div>
    <div class="line-big">EXPERTS</div>
    <div class="rule"></div>
  </div>
  <footer class="page-footer"><svg viewBox="0 0 379 39"><use href="#footer-band"/></svg><span class="url">www.kestle.example</span></footer>
</section>

<section class="page page--services">
  <header class="page-header">
    <div class="wordmark"><span class="wordmark-name">KESTLE</span><span class="wordmark-tag">PLUMBING &amp; HEATING</span></div>
    <span class="brand-dot"></span>
  </header>
  <div class="hero-banner" role="img" aria-label="Blue photo of rippling water"></div>
  <h1 class="hero-title">Caring for<br>your essential<br>home services</h1>
  <div class="service-grid">
    <div class="service-tile">
      <svg class="service-icon" viewBox="0 0 36 36" role="img" aria-label="Central heating icon"><path d="M18 3 L34 18 L30 18 L30 34 L6 34 L6 18 L2 18 Z" fill="url(#iconFlame)"/><path d="M13 22 q-2 3 0 5 q2 2 0 5 M18 22 q-2 3 0 5 q2 2 0 5 M23 22 q-2 3 0 5 q2 2 0 5" fill="none" stroke="#fff" stroke-width="1.4" stroke-linecap="round"/></svg>
      <span class="service-name">Central Heating</span></div>
    <div class="service-tile">
      <svg class="service-icon" viewBox="0 0 36 36" role="img" aria-label="Boiler icon"><rect x="9" y="2" width="18" height="29" rx="2" fill="url(#iconFlame)"/><rect x="12" y="31" width="3" height="4" fill="#e8321f"/><rect x="21" y="31" width="3" height="4" fill="#e8321f"/><path d="M18 9 q4 5 0 9 q-4 -4 0 -9z" fill="#fff"/><rect x="12" y="23" width="12" height="2" fill="#fff"/></svg>
      <span class="service-name">Boilers</span></div>
    <div class="service-tile">
      <svg class="service-icon" viewBox="0 0 36 36" role="img" aria-label="Tap icon"><rect x="14" y="3" width="12" height="3" rx="1.5" fill="#f47a20"/><rect x="19" y="5" width="2" height="6" fill="#f47a20"/><rect x="3" y="12" width="7" height="13" fill="url(#iconFlame)"/><path d="M10 12 L26 12 Q33 12 33 19 L33 25 L26 25 L26 20 L10 20 Z" fill="url(#iconFlame)"/><path d="M29.5 28 q2 3 0 5 q-2 -2 0 -5z" fill="#1f7ae0"/></svg>
      <span class="service-name">General Plumbing</span></div>
    <div class="service-tile">
      <svg class="service-icon" viewBox="0 0 36 36" role="img" aria-label="Bath and shower icon"><path d="M26 16 L26 6 Q26 3 29 3 L31 3" fill="none" stroke="#f47a20" stroke-width="2"/><path d="M21 9 l5 -3 l0 6 z" fill="#f47a20"/><rect x="2" y="17" width="32" height="3" rx="1.5" fill="#f47a20"/><path d="M4 20 L32 20 L30 28 Q29 31 26 31 L10 31 Q7 31 6 28 Z" fill="url(#iconFlame)"/><rect x="9" y="31" width="3" height="3" fill="#e8321f"/><rect x="24" y="31" width="3" height="3" fill="#e8321f"/></svg>
      <span class="service-name">Bathrooms</span></div>
    <div class="service-tile">
      <svg class="service-icon" viewBox="0 0 36 36" role="img" aria-label="Radiator icon"><path d="M9 2 q-2 3 0 5 q2 2 0 5 M15 2 q-2 3 0 5 q2 2 0 5 M21 2 q-2 3 0 5 q2 2 0 5 M27 2 q-2 3 0 5 q2 2 0 5" fill="none" stroke="#f47a20" stroke-width="1.4" stroke-linecap="round"/><g fill="url(#iconFlame)"><rect x="5" y="14" width="4" height="20" rx="2"/><rect x="10.5" y="14" width="4" height="20" rx="2"/><rect x="16" y="14" width="4" height="20" rx="2"/><rect x="21.5" y="14" width="4" height="20" rx="2"/><rect x="27" y="14" width="4" height="20" rx="2"/></g></svg>
      <span class="service-name">Power Flushing</span></div>
    <div class="service-tile">
      <svg class="service-icon" viewBox="0 0 36 36" role="img" aria-label="Underfloor pipework icon"><rect x="4" y="2" width="28" height="9" fill="#f7a35c"/><path d="M8 14 L28 14 Q31 14 31 17 Q31 20 28 20 L8 20 Q5 20 5 23 Q5 26 8 26 L28 26 Q31 26 31 29 Q31 32 28 32 L6 32" fill="none" stroke="url(#iconFlame)" stroke-width="3"/></svg>
      <span class="service-name">Underfloor Heating</span></div>
    <div class="service-tile">
      <svg class="service-icon" viewBox="0 0 36 36" role="img" aria-label="Gas bottle icon"><rect x="14" y="1" width="8" height="4" fill="#f47a20"/><rect x="12" y="5" width="12" height="4" rx="1" fill="#f47a20"/><rect x="8" y="9" width="20" height="25" rx="8" fill="url(#iconFlame)"/><circle cx="18" cy="21" r="6" fill="#fff"/><path d="M18 17 q3 3 0 7 q-3 -4 0 -7z" fill="#e8321f"/></svg>
      <span class="service-name">LPG</span></div>
    <div class="service-tile">
      <svg class="service-icon" viewBox="0 0 36 36" role="img" aria-label="Boiler installation icon"><path d="M10 14 L10 4 L26 4 L26 8" fill="none" stroke="#f47a20" stroke-width="2.2"/><rect x="4" y="14" width="28" height="16" rx="2" fill="url(#iconFlame)"/><circle cx="22" cy="21" r="2.6" fill="#fff"/><circle cx="28" cy="21" r="2.6" fill="#fff"/><rect x="8" y="30" width="3" height="5" fill="#e8321f"/><rect x="25" y="30" width="3" height="5" fill="#e8321f"/></svg>
      <span class="service-name">Boiler Installation</span></div>
  </div>
  <footer class="page-footer"><svg viewBox="0 0 379 39"><use href="#footer-band"/></svg><span class="url">www.kestle.example</span></footer>
</section>

<section class="page page--welcome">
  <header class="page-header">
    <div class="wordmark"><span class="wordmark-name">KESTLE</span><span class="wordmark-tag">PLUMBING &amp; HEATING</span></div>
    <span class="brand-dot"></span>
  </header>
  <h1 class="welcome-title">Welcome<br>to Kestle<br>Plumbing &amp; Heating</h1>
  <div class="about-box">
    <p>Kestle Plumbing &amp; Heating was originally founded by Daniel Kestle, later joined by his son and have been providing plumbing &amp; heating solutions in Harwick Bay, Saltmere, Ashcombe and surrounding areas of Wessex since 1978. We are a friendly, family run company combining traditional values with a modern outlook.</p>
    <p>We aim to provide our clients with great advice, excellent service, quality materials and workmanship that is second to none for all your plumbing, heating and gas requirements. Our experienced engineers are GasCert Registered and proud members, Registered Plumbers and Heating Professionals with the IHPE.</p>
    <p>The majority of our work comes through recommendation and returning clients, so our reputation is extremely important to us.</p>
    <p>Call Kestle Plumbing &amp; Heating to discuss your requirements, or book an appointment with one of our team today.</p>
  </div>
  <div class="seal">
    <span class="name">KESTLE</span>
    <span class="tag">PLUMBING &amp; HEATING</span>
  </div>
  <div class="feature" style="top:327px">
    <svg width="13" height="16" viewBox="0 0 13 16"><path d="M6.5 0.5a6 6 0 0 1 6 6c0 4-6 9-6 9s-6-5-6-9a6 6 0 0 1 6-6z" fill="var(--orange)"/><circle cx="6.5" cy="6.5" r="2.3" fill="#fff"/></svg>
    <h3>Based in Harwick Bay and Saltmere, Wessex</h3>
    <p>Offering our services throughout Wessex including Harwick Bay, Saltmere, Ashcombe, Marlow Vale, Fenwick and surrounding areas.</p>
  </div>
  <div class="feature" style="top:378px">
    <svg width="15" height="15" viewBox="0 0 15 15"><path d="M2 13 L9 6" stroke="var(--orange)" stroke-width="2.4" stroke-linecap="round"/><circle cx="10.5" cy="4.5" r="3.2" fill="none" stroke="var(--orange)" stroke-width="2"/><path d="M2 2 L13 13" stroke="var(--red)" stroke-width="1.6" stroke-linecap="round"/></svg>
    <h3>Committed to Quality</h3>
    <p>Our range of plumbing &amp; heating services come with the peace of mind that we always use quality materials. Coupled with our unrivaled workmanship, we always strive to exceed our clients' expectations.</p>
  </div>
  <div class="feature" style="top:435px">
    <svg width="15" height="15" viewBox="0 0 15 15"><circle cx="7.5" cy="7.5" r="6.5" fill="var(--orange)"/><path d="M4.3 7.7 L6.6 10 L10.8 5.3" fill="none" stroke="#fff" stroke-width="1.6" stroke-linecap="round" stroke-linejoin="round"/></svg>
    <h3>Up To 10 Year Boiler Guarantees</h3>
    <p>As Northvale Accredited Installers and Corvane Selected Partners, we are able to offer guarantees of up to 10 years on the boilers we install. Other boiler makes are also available to suit every budget.</p>
  </div>
  <footer class="page-footer"><svg viewBox="0 0 379 39"><use href="#footer-band"/></svg><span class="url">www.kestle.example</span></footer>
</section>

<section class="page page--reviews">
  <header class="page-header">
    <div class="wordmark"><span class="wordmark-name">KESTLE</span><span class="wordmark-tag">PLUMBING &amp; HEATING</span></div>
    <span class="brand-dot"></span>
  </header>
  <h1 class="reviews-title">REVIEWS</h1>
  <div class="review-grid">
    <article class="review">
      <div class="stars">★★★★★</div>
      <div class="title">friendly and professional serv...</div>
      <div class="date">May 31st, 2018</div>
      <div class="verified">Verified by trade listing</div>
      <div class="ratings"><div><span>Time management</span><span>★★★★★</span></div><div><span>Tidiness</span><span>★★★★★</span></div><div><span>Friendly Rating</span><span>★★★★★</span></div><div><span>Value Rating</span><span>★★★★★</span></div></div>
      <p class="body">I rang Kestle and they came out the same day. Quick, tidy work and the old tap was fixed within the hour.</p>
      <div class="share-bar">Share :</div>
    </article>
    <article class="review">
      <div class="stars">★★★★★</div>
      <div class="title">Good jobs good prices</div>
      <div class="date">January 15th, 2015</div>
      <div class="ratings"><div><span>Time management</span><span>★★★★★</span></div><div><span>Tidiness</span><span>★★★★★</span></div><div><span>Friendly Rating</span><span>★★★★★</span></div><div><span>Value Rating</span><span>★★★★★</span></div></div>
      <p class="body">The engineer is brilliant, he looks after us and my family too. Good jobs, good prices.</p>
      <div class="share-bar">Share :</div>
    </article>
    <article class="review">
      <div class="stars">★★★★★</div>
      <div class="title">Local friendly service</div>
      <div class="date">December 30th, 2014</div>
      <div class="ratings"><div><span>Time management</span><span>★★★★★</span></div><div><span>Tidiness</span><span>★★★★★</span></div><div><span>Friendly Rating</span><span>★★★★★</span></div><div><span>Value Rating</span><span>★★★★★</span></div></div>
      <p class="body">Family run and friendly service. Have completed lots of work at our house, always competitively priced and very tidy.</p>
      <div class="share-bar">Share :</div>
    </article>
    <article class="review">
      <div class="stars">★★★★★</div>
      <div class="title">Will definitely be using again</div>
      <div class="date">March 14th, 2015</div>
      <div class="ratings"><div><span>Time management</span><span>★★★★★</span></div><div><span>Tidiness</span><span>★★★★★</span></div><div><span>Friendly Rating</span><span>★★★★★</span></div><div><span>Value Rating</span><span>★★★★★</span></div></div>
      <p class="body">Had an issue with my boiler and they came within the hour. Fixed the fault and gave superb advice. Will use again.</p>
      <div class="share-bar">Share :</div>
    </article>
    <article class="review">
      <div class="stars">★★★★★</div>
      <div class="title">Will 100% recommend</div>
      <div class="date">January 22nd, 2016</div>
      <div class="ratings"><div><span>Time management</span><span>★★★★★</span></div><div><span>Tidiness</span><span>★★★★★</span></div><div><span>Friendly Rating</span><span>★★★★★</span></div><div><span>Value Rating</span><span>★★★★★</span></div></div>
      <p class="body">Simply awesome, same day service and very polite staff who explained clearly what the fault was. Will 100% recommend.</p>
      <div class="share-bar">Share :</div>
    </article>
    <article class="review">
      <div class="stars">★★★★★</div>
      <div class="title">Really friendly, good communic...</div>
      <div class="date">October 15th, 2016</div>
      <div class="ratings"><div><span>Time management</span><span>★★★★★</span></div><div><span>Tidiness</span><span>★★★★★</span></div><div><span>Friendly Rating</span><span>★★★★★</span></div><div><span>Value Rating</span><span>★★★★★</span></div></div>
      <p class="body">Really friendly, good communication from start to finish and work to a high standard. Will be using again.</p>
      <div class="share-bar">Share :</div>
    </article>
  </div>
  <div class="partner-row">
    <span class="partner partner--a" role="img" aria-label="Accredited installer badge"></span>
    <span class="partner partner--b" role="img" aria-label="Boiler manufacturer partner badge"></span>
    <span class="partner partner--c" role="img" aria-label="Selected partner badge"></span>
    <span class="partner partner--d" role="img" aria-label="Gas registration badge"></span>
  </div>
  <footer class="page-footer"><svg viewBox="0 0 379 39"><use href="#footer-band"/></svg><span class="url">www.kestle.example</span></footer>
</section>

</body>
</html>
```